Refresh Application User Interface

Brindlecove wishes to update the look of its business applications. Two representative forms are shown below. Please note, we are not considering changes in functionality or usability. Our goal is a cleaner, more contemporary design.

Industry/Entity Type

Business

```html
<!DOCTYPE html>
<html lang="en">
<head>
<meta charset="utf-8">
<title>Brindlecove – Purchase Order Lines</title>
<link href="https://fonts.googleapis.com/css2?family=Source+Sans+3:wght@400;600;700&display=swap" rel="stylesheet">
<style>
:root{
  --green:#8dc84f;
  --charcoal:#262626;
  --page:#efefef;
  --panel:#e4e4e4;
  --white:#ffffff;
  --row:#f6f6f6;
  --ink:#222222;
  --link:#1f5bab;
  --navy:#0d2f8a;
  --pill-blue:#1550a6;
  --pill-green:#17662a;
  --amber:#fbb424;
  --over:#f2897a;
  --pending:#f6c46c;
  --btn-grey:#6b6b6b;
  --icon:#6d6d6d;
}
*{box-sizing:border-box;margin:0;padding:0}
html,body{width:1200px;height:1200px;overflow:hidden}
body{font-family:"Source Sans 3",sans-serif;color:var(--ink);background:var(--page);position:relative}
.abs{position:absolute}
.band-top{top:0;left:0;width:1200px;height:14px;background:linear-gradient(90deg,#5fae5a,#7dbd58 50%,#3f9a73)}
.band-bottom{bottom:0;left:0;width:1200px;height:22px;background:linear-gradient(90deg,#2e7f7a,#2a6f86 50%,#3e8a6a)}
.userbar{top:14px;left:0;width:1200px;height:36px;background:var(--charcoal);color:#fff;font-size:12px;font-weight:600;display:flex;align-items:center;padding:0 34px 0 30px}
.userbar .sep{width:1px;height:20px;background:#555;margin:0 16px 0 19px}
.userbar .utils{margin-left:auto;display:flex;gap:26px;font-weight:400}
.masthead{top:50px;left:0;width:1200px;height:64px;background:var(--white)}
.brand{left:28px;top:14px;font-size:30px;font-weight:700;color:var(--navy);letter-spacing:.5px}
.modules{top:0;height:64px;font-size:16px;color:var(--link)}
.modules a{text-decoration:none;color:inherit;position:absolute;top:22px;transform:translateX(-50%);white-space:nowrap}
.modules .active{top:0;height:64px;width:96px;background:var(--green);color:#fff;display:flex;align-items:center;justify-content:center;transform:none}
.subnav{top:114px;left:0;width:1200px;height:54px;background:var(--green);display:flex;align-items:center;justify-content:space-between;padding:0 33px 0 21px;color:#fff;font-size:16px}
.titlebar{top:188px;left:30px;width:1136px;height:54px;background:var(--panel);display:flex;align-items:center;padding:0 25px}
.titlebar h1{font-size:18px;font-weight:600;color:#444}
.tabs{margin-left:auto;display:flex;gap:29px;font-size:13px;color:#999;margin-right:24px}
.tabs .on{color:var(--link);font-weight:700}
.card{background:var(--white);left:30px;width:1136px}
.toolbar{top:260px;height:80px}
.back{left:27px;top:26px;font-size:18px;font-weight:700;color:var(--link)}
.vsep{left:98px;top:18px;width:1px;height:44px;background:#ddd}
.search{left:136px;top:22px;width:288px;height:36px;border:1px solid #ccc;font-size:13px;color:#888;padding:9px 16px}
.search svg{position:absolute;right:10px;top:9px}
.tool{top:26px}
.action{top:27px;display:flex;align-items:center;gap:6px;font-size:16px;color:var(--link)}
.btn-new{left:1017px;top:22px;width:84px;height:36px;border:1.5px solid var(--link);color:var(--link);font-size:16px;font-weight:700;display:flex;align-items:center;justify-content:center}
.order{top:350px;height:164px}
.order-no{left:25px;top:24px;font-size:31px;font-weight:400;color:#333}
.label{font-size:14px;color:#333}
.pill{border-radius:12px;color:#fff;font-size:13px;font-weight:600;padding:3px 16px}
.pill-green{background:var(--pill-green)}
.pill-amber{background:var(--amber);color:#333;font-weight:400;padding:3px 22px}
.gridbar{top:536px;height:80px}
.gicon{top:24px}
.pager{right:24px;top:28px;display:flex;align-items:center;font-size:15px;color:#555}
.lines{top:624px;height:450px;background:var(--white)}
.th{top:28px;font-size:18px;font-weight:600;color:#222}
.checkbox{width:24px;height:24px;border:1.5px solid #999;border-radius:2px;background:#fff}
.line{left:0;width:1136px;height:178px;background:var(--row)}
.sku{border-radius:12px;background:var(--pill-blue);color:#fff;font-size:14px;padding:2px 16px;top:14px;left:87px}
.desc{left:87px;top:46px;font-size:15px;line-height:26.5px;width:300px}
.select{background:#fff;height:34px;display:flex;align-items:center;font-size:15px;padding:0 12px}
.select svg{margin-left:auto}
.num{font-size:15px;text-align:center;width:120px}
.note{font-size:13px;text-align:center;width:120px}
.over{color:var(--over)}
.pend{color:var(--pending)}
.alch{font-size:17px;font-weight:700;color:var(--navy)}
.btn{height:35px;display:flex;align-items:center;justify-content:center;color:#fff;font-size:17px;font-weight:600;top:1102px}
.apply{left:942px;width:91px;background:var(--green)}
.cancel{left:1051px;width:97px;background:var(--btn-grey)}
</style>
</head>
<body>
<div class="abs band-top"></div>

<header class="abs userbar">
  <span>Welcome, Dana Whitfield</span><span class="sep"></span><span>Current Role : Administrator</span>
  <nav class="utils"><span>Touch</span><span>New Tab</span><span>Help</span><span>Support</span><span>Logout</span></nav>
</header>

<div class="abs masthead">
  <div class="abs brand">Brindlecove</div>
  <nav class="modules abs" style="left:0;width:1200px">
    <a style="left:441px">Home</a>
    <a style="left:541px">eSource</a>
    <a class="active" style="left:590px">eBuy</a>
    <a style="left:738px">eRequest</a>
    <a style="left:838px">eSell</a>
    <a style="left:930px">eStock</a>
    <a style="left:1025px">ePlan</a>
    <a style="left:1132px">Prefrences</a>
  </nav>
</div>

<nav class="abs subnav">
  <span>Orders</span><span>Receipts</span><span>Shipments</span><span>Invoices</span><span>Pricing</span><span>Tables</span><span>Reports</span><span>Inquries</span><span>Periodic Tasks</span><span>Workflow</span>
</nav>

<section class="abs titlebar">
  <h1>Purchase Order</h1>
  <div class="tabs"><span>Header</span><span class="on">Lines</span><span>Charges</span><span>Notes</span></div>
</section>

<section class="abs card toolbar">
  <div class="abs back">Back</div>
  <div class="abs vsep"></div>
  <div class="abs search">Search
    <svg width="18" height="18" viewBox="0 0 18 18" fill="none" stroke="#1f5bab" stroke-width="2"><circle cx="7.5" cy="7.5" r="5.5"/><path d="M11.5 11.5l5 5"/></svg>
  </div>
  <svg class="abs tool" style="left:449px" width="26" height="28" viewBox="0 0 26 28" fill="none" stroke="#6d6d6d" stroke-width="2"><path d="M18 8L8.5 17.5a3 3 0 004.2 4.2L22 12.5a5.5 5.5 0 00-7.8-7.8L4.8 14.1a8 8 0 0011.3 11.3"/></svg>
  <svg class="abs tool" style="left:500px" width="30" height="30" viewBox="0 0 30 30" fill="none" stroke="#6d6d6d" stroke-width="2"><path d="M16 27H3V2h13l6 6v6"/><path d="M16 2v6h6"/><circle cx="19" cy="20" r="4.5"/><path d="M22.3 23.3L27 28"/></svg>
  <svg class="abs tool" style="left:553px" width="28" height="28" viewBox="0 0 28 28" fill="none" stroke="#6d6d6d" stroke-width="2"><circle cx="5" cy="14" r="3.5"/><circle cx="21" cy="5" r="3.5"/><circle cx="21" cy="23" r="3.5"/><path d="M8 12.3l10-5.5M8 15.7l10 5.5"/></svg>
  <svg class="abs tool" style="left:604px" width="30" height="28" viewBox="0 0 30 28" fill="#6d6d6d"><path d="M2 10h26l-3 15H5z"/><path d="M9 10l5-8M21 10l-5-8" stroke="#6d6d6d" stroke-width="2"/><path d="M9 13v9M13 13v9M17 13v9M21 13v9" stroke="#fff" stroke-width="1.6"/></svg>
  <svg class="abs tool" style="left:656px" width="28" height="28" viewBox="0 0 28 28" fill="none" stroke="#6d6d6d" stroke-width="1.6"><circle cx="14" cy="14" r="12"/><path d="M10.5 11a3.5 3.5 0 117 0c0 2.5-3.5 2.8-3.5 5.5"/><circle cx="14" cy="20" r=".8" fill="#6d6d6d"/></svg>
  <div class="abs action" style="left:715px">
    <svg width="26" height="26" viewBox="0 0 26 26" fill="#1f5bab"><path d="M17 1a7 7 0 00-6.5 9.5L1.5 19.5a2.8 2.8 0 004 4l9-9A7 7 0 0024 7.5l-4 4-4-1-1-4 4-4A7 7 0 0017 1z"/></svg>
    <span>View GL Account</span>
  </div>
  <div class="abs action" style="left:889px">
    <svg width="26" height="26" viewBox="0 0 26 26" fill="none" stroke="#1f5bab" stroke-width="2.2"><path d="M13 4H3v19h19V13"/><path d="M21 2l3 3-11 11-4 1 1-4z"/></svg>
    <span>Post Offer</span>
  </div>
  <div class="abs btn-new">New</div>
</section>

<section class="abs card order">
  <div class="abs order-no">Order Number : 100159</div>
  <div class="abs label" style="left:25px;top:72px">Order Type :</div>
  <div class="abs pill pill-green" style="left:109px;top:70px">Regular Purchase Order</div>
  <div class="abs label" style="left:42px;top:107px">Address :</div>
  <div class="abs label" style="left:108px;top:107px">Harborline Supply Co., Eastbrook MA</div>
  <div class="abs label" style="left:873px;top:35px">Status :</div>
  <div class="abs pill pill-amber" style="left:931px;top:33px">Hold for Completion</div>
</section>

<section class="abs card gridbar">
  <svg class="abs gicon" style="left:27px" width="26" height="30" viewBox="0 0 26 30" fill="#6d6d6d"><path d="M1 1h24v6h-2.5l-1-3H7l9 11-9 11h15l1-3H25v6H1v-2l10-12L1 3z"/></svg>
  <svg class="abs gicon" style="left:82px" width="26" height="30" viewBox="0 0 26 30" fill="none" stroke="#6d6d6d" stroke-width="2"><path d="M17 5V1H2v22h5"/><path d="M8 6h15v23H8z"/></svg>
  <svg class="abs gicon" style="left:136px" width="28" height="28" viewBox="0 0 28 28" fill="#6d6d6d"><path d="M5 2h18v3H5zM3 7h22v3H3z"/><path d="M1 12h8l2 4h6l2-4h8v14H1z"/></svg>
  <svg class="abs gicon" style="left:191px" width="26" height="28" viewBox="0 0 26 28" fill="#6d6d6d"><path d="M1 2h24v4l-9 9v11l-6-3v-8L1 6z"/></svg>
  <svg class="abs gicon" style="left:249px" width="26" height="26" viewBox="0 0 26 26" stroke="#6d6d6d" stroke-width="2.4"><path d="M2 2l22 22M24 2L2 24"/></svg>
  <div class="abs pager">
    <span style="margin-right:38px">Page 1 of&nbsp; 2</span>
    <svg width="14" height="20" viewBox="0 0 14 20" fill="none" stroke="#888" stroke-width="1.6"><path d="M11 2L3 10l8 8"/></svg>
    <span style="margin:0 27px 0 24px;color:var(--link);font-weight:600">1</span>
    <span style="margin-right:24px">2</span>
    <svg width="14" height="20" viewBox="0 0 14 20" fill="none" stroke="#888" stroke-width="1.6"><path d="M3 2l8 8-8 8"/></svg>
  </div>
</section>

<section class="abs card lines">
  <div class="abs checkbox" style="left:27px;top:29px"></div>
  <div class="abs th" style="left:87px">Product</div>
  <div class="abs th" style="left:457px">Unit Price</div>
  <div class="abs th" style="left:596px">Unit Price</div>
  <div class="abs th" style="left:746px">Quantity</div>
  <div class="abs th" style="left:879px">Available</div>
  <div class="abs th" style="left:1012px">Extended</div>

  <div class="abs line" style="top:84px">
    <div class="abs checkbox" style="left:27px;top:18px"></div>
    <div class="abs sku">P-1200</div>
    <div class="abs desc">Northmill 471582 - Flyer Stock Paper,<br>Satin Finish Text,<br>8&nbsp; 1/2” X&nbsp; 11”,&nbsp; 24 lb.,<br>94 Brightness</div>
    <div class="abs select" style="left:458px;top:14px;width:66px">EA<svg width="8" height="6"><path d="M0 0h8L4 5z" fill="#0d2f8a"/></svg></div>
    <div class="abs num" style="left:570px;top:21px">$ 6.54</div>
    <div class="abs note over" style="left:570px;top:46px">Over Budget</div>
    <div class="abs select" style="left:755px;top:14px;width:66px">30<svg width="8" height="6"><path d="M0 0h8L4 5z" fill="#0d2f8a"/></svg></div>
    <div class="abs num" style="left:850px;top:21px">0</div>
    <div class="abs num" style="left:992px;top:21px">$ 6.54</div>
    <div class="abs note pend" style="left:992px;top:46px">Pending</div>
    <div class="abs alch" style="left:820px;top:123px">ALCH</div>
    <div class="abs select" style="left:897px;top:117px;width:194px;font-size:16px">Receive &amp; Pay<svg width="8" height="6"><path d="M0 0h8L4 5z" fill="#0d2f8a"/></svg></div>
  </div>

  <div class="abs line" style="top:266px">
    <div class="abs checkbox" style="left:27px;top:18px"></div>
    <div class="abs sku">P-1200</div>
    <div class="abs desc">Northmill 471582 - Flyer Stock Paper,<br>Satin Finish Text,<br>8&nbsp; 1/2” X&nbsp; 11”,&nbsp; 24 lb.,<br>94 Brightness</div>
    <div class="abs select" style="left:458px;top:14px;width:66px">EA<svg width="8" height="6"><path d="M0 0h8L4 5z" fill="#0d2f8a"/></svg></div>
    <div class="abs num" style="left:570px;top:21px">$ 6.54</div>
    <div class="abs note over" style="left:570px;top:46px">Over Budget</div>
    <div class="abs select" style="left:755px;top:14px;width:66px">30<svg width="8" height="6"><path d="M0 0h8L4 5z" fill="#0d2f8a"/></svg></div>
    <div class="abs num" style="left:850px;top:21px">0</div>
    <div class="abs num" style="left:992px;top:21px">$ 6.54</div>
    <div class="abs note pend" style="left:992px;top:46px">Pending</div>
    <div class="abs alch" style="left:820px;top:123px">ALCH</div>
    <div class="abs select" style="left:897px;top:117px;width:194px;font-size:16px">Receive &amp; Pay<svg width="8" height="6"><path d="M0 0h8L4 5z" fill="#0d2f8a"/></svg></div>
  </div>
</section>

<div class="abs btn apply">Apply</div>
<div class="abs btn cancel">Cancel</div>

<div class="abs band-bottom"></div>
</body>
</html>
```